Business card

We are looking for a creative person to deigns our company business card.

Target Market(s)

College age student

Industry/Entity Type

Accommodation

Contact Information for Business Card

We want a fun, clean and sophisticated design. It should look good, but more importantly the information should be legible.

Font styles to use
Serif
Sans Serif
Other font styles liked:
• Open Sans ,

Colors
33a6d7

Requirements
Must have
• Must have a young and memorable message. Be legible.
• Our logo on the back on a solid blue , please find color and logo attached
• LodgeBridgely.net on the back.
Nice to have
• I would like to have couple of different fonts on the LodgeBridgely.net on the back of the cards with a solid blue.

```html
<!DOCTYPE html>
<html lang="en">
<head>
<meta charset="UTF-8">
<title>LodgeBridgely.net – Business Card</title>
<link href="https://fonts.googleapis.com/css2?family=Lato:wght@400;700&family=Open+Sans:wght@600;700&display=swap" rel="stylesheet">
<style>
  :root {
    --navy: #053853;
    --navy-deep: #023550;
    --sky: #3597d3;
    --brand-blue: #33a6d7;
    --paper: #ffffff;
    --paper-shade: #eef0f2;
    --ghost: #dcdfe2;
    --stage-light: #ececec;
    --stage-dark: #c9c9c9;
  }
  * { margin: 0; padding: 0; box-sizing: border-box; }
  html, body { width: 1200px; height: 675px; overflow: hidden; }
  body {
    background: radial-gradient(ellipse at 40% 35%, var(--stage-light), var(--stage-dark));
    display: flex;
    align-items: center;
    justify-content: center;
    gap: 60px;
  }
  .card {
    position: relative;
    width: 500px;
    height: 286px;
    overflow: hidden;
    box-shadow: 0 10px 26px rgba(0,0,0,.18);
  }

  /* Back side */
  .card-back {
    background: var(--navy-deep);
    display: flex;
    align-items: center;
    justify-content: center;
  }
  .brand-name {
    font-family: "Open Sans", sans-serif;
    font-weight: 700;
    font-size: 34px;
    color: var(--brand-blue);
    letter-spacing: .2px;
  }

  /* Front side */
  .card-front {
    background: linear-gradient(120deg, var(--paper) 45%, var(--paper-shade));
  }
  .header-shape { position: absolute; inset: 0; }
  .identity {
    position: absolute;
    top: 30px;
    left: 34px;
    display: flex;
    align-items: center;
    gap: 12px;
    color: var(--paper);
  }
  .avatar { width: 44px; height: 44px; }
  .person-name {
    font-family: "Lato", sans-serif;
    font-weight: 400;
    font-size: 27px;
    line-height: 1;
    letter-spacing: .5px;
  }
  .person-role {
    font-family: "Lato", sans-serif;
    font-size: 14px;
    margin-top: 3px;
  }
  .contact-list {
    position: absolute;
    top: 168px;
    left: 22px;
    list-style: none;
    font-family: "Open Sans", sans-serif;
    font-weight: 600;
    font-size: 14.5px;
    color: var(--navy);
  }
  .contact-item {
    display: flex;
    align-items: center;
    gap: 8px;
    height: 26px;
  }
  .contact-icon { width: 20px; height: 20px; flex: none; }
  .ghost-name {
    position: absolute;
    right: 22px;
    bottom: 40px;
    font-family: "Open Sans", sans-serif;
    font-weight: 700;
    font-size: 22px;
    color: var(--ghost);
  }
</style>
</head>
<body>

  <section class="card card-back" aria-label="Card back">
    <span class="brand-name">LodgeBridgely.net</span>
  </section>

  <section class="card card-front" aria-label="Card front">
    <svg class="header-shape" viewBox="0 0 500 286" aria-hidden="true">
      <path d="M0 100 L0 132 L250 168 C300 168 350 150 380 118 L380 100 Z" fill="var(--sky)"/>
      <path d="M0 0 H420 C395 95 345 150 270 152 C250 152 232 150 210 146 L0 112 Z" fill="var(--navy)"/>
    </svg>

    <div class="identity">
      <svg class="avatar" viewBox="0 0 44 44" aria-hidden="true">
        <circle cx="22" cy="22" r="21" fill="var(--paper)"/>
        <circle cx="22" cy="17" r="6.5" fill="var(--navy)"/>
        <path d="M11 33 C12 25 32 25 33 33 Z" fill="var(--navy)"/>
      </svg>
      <div>
        <div class="person-name">ROWAN VALE</div>
        <div class="person-role">The Creative Designer</div>
      </div>
    </div>

    <ul class="contact-list">
      <li class="contact-item">
        <svg class="contact-icon" viewBox="0 0 20 20" aria-hidden="true">
          <circle cx="10" cy="10" r="10" fill="var(--navy)"/>
          <path d="M7 5 L9 7.5 L8 9 C8.8 10.6 9.6 11.4 11 12 L12.5 11 L15 13 L14 15 C10 15 5 10 5 6 Z" fill="var(--paper)"/>
        </svg>
        <span>+1 555 014 2286</span>
      </li>
      <li class="contact-item">
        <svg class="contact-icon" viewBox="0 0 20 20" aria-hidden="true">
          <circle cx="10" cy="10" r="10" fill="var(--navy)"/>
          <rect x="5" y="6.5" width="10" height="7" fill="var(--paper)"/>
          <path d="M5 6.5 L10 10.5 L15 6.5" fill="none" stroke="var(--navy)" stroke-width="1"/>
        </svg>
        <span>rowan.vale@mailbox.test</span>
      </li>
      <li class="contact-item">
        <svg class="contact-icon" viewBox="0 0 20 20" aria-hidden="true">
          <circle cx="10" cy="10" r="10" fill="var(--navy)"/>
          <g fill="none" stroke="var(--paper)" stroke-width="1.2">
            <circle cx="10" cy="10" r="5.5"/>
            <ellipse cx="10" cy="10" rx="2.4" ry="5.5"/>
            <path d="M4.5 10 H15.5"/>
          </g>
        </svg>
        <span>www.lodgebridgely.net</span>
      </li>
      <li class="contact-item">
        <svg class="contact-icon" viewBox="0 0 20 20" aria-hidden="true">
          <circle cx="10" cy="10" r="10" fill="var(--navy)"/>
          <path d="M10 15.5 C7 12 6.5 10.5 6.5 8.5 A3.5 3.5 0 0 1 13.5 8.5 C13.5 10.5 13 12 10 15.5 Z" fill="var(--paper)"/>
          <circle cx="10" cy="8.5" r="1.3" fill="var(--navy)"/>
        </svg>
        <span>USA, Maple Row 48/2</span>
      </li>
    </ul>

    <span class="ghost-name">LodgeBridgely.net</span>
  </section>

</body>
</html>
```